I am writing a book called "SMILING OPENS EVERY DOOR "

I NEED A BOOK COVER FOR MY BOOK" SMILING OPENS EVERY DOOR"
so So Who Knocked First? " ( this in smaller font)

"Smiling Opens Every Door " will need to designed to eventually be a logo , banner and business card
COLOURS MAINLY ORANGE AND WHITE (with accents bright colour )

THE BOOK IS MY LAUGHTER JOURNEY AS A PERFORMER AND ADVENTURE INDIA LEARNING ABOUT LAUGHTER YOGA WHICH I WILL BE TEACHING

I do not want photos on the front cover ..
The look could be modern and eye-catching
I have also just been to India to learn Laughing Yoga with Dr Tobin Verhaal

Thank-you so much everyone for your brilliant designs . i am overwhelmed with your talent . i hope to work with you all again soon ! Marnie  

Target Market(s)

"Adults based in western speaking countries aged 25 to 60 that want to learn to laugh more
Also this book will be sold at my conference workshops

Industry/Entity Type

Business

Requirements
Must have
• ORANGE AND WHITE
CAN HAVE AQUA , HOT PINK , LIME GREEN, YELLOW ACCENTS

THESE WILL BE DIFFERENT AREAS WILL COVERING IN MY BOOK
EG LAUGHTER NAD BREAT CANCER ( PINK)
LAUGHTER NAD DEPRESSION ( BLUE)
LAUGHTER AND KIDS ( YELLOW)

NO Photos on front cover
Should not have
• No photos

```html
<!DOCTYPE html>
<html lang="en">
<head>
<meta charset="utf-8">
<title>Smiling Opens Every Door – Book Cover</title>
<link rel="stylesheet" href="https://fonts.googleapis.com/css2?family=Open+Sans:wght@400;600&display=swap">
<style>
  :root {
    --page-bg: #f3f3f1;
    --orange-light: #fbbf2a;
    --orange-mid: #f5aa1c;
    --orange-deep: #e39a12;
    --white: #ffffff;
    --panel-white: #f4f6f6;
    --shadow: rgba(60, 40, 0, 0.18);
  }
  * { margin: 0; padding: 0; box-sizing: border-box; }
  html, body {
    width: 1200px;
    height: 1000px;
    overflow: hidden;
    background: var(--page-bg);
  }
  .canvas {
    position: relative;
    width: 1200px;
    height: 1000px;
  }
  .cover {
    position: absolute;
    left: 280px;
    top: 60px;
    width: 640px;
    height: 880px;
    background: linear-gradient(150deg, var(--orange-light) 0%, var(--orange-mid) 55%, var(--orange-deep) 100%);
    box-shadow: 0 18px 40px var(--shadow);
    font-family: "Open Sans", Arial, sans-serif;
    color: var(--white);
    overflow: hidden;
  }
  .title { font-weight: 400; }
  .title-top {
    position: absolute;
    left: 40px;
    top: 34px;
    font-size: 58px;
    font-weight: 400;
    letter-spacing: 2px;
    line-height: 1;
  }
  .frame-upright {
    position: absolute;
    left: 40px;
    top: 120px;
    width: 84px;
    height: 660px;
    background: var(--panel-white);
  }
  .frame-base {
    position: absolute;
    left: 40px;
    top: 650px;
    width: 560px;
    height: 130px;
    background: var(--panel-white);
  }
  .subtitle {
    position: absolute;
    left: 124px;
    top: 650px;
    width: 476px;
    height: 130px;
    display: flex;
    align-items: center;
    justify-content: flex-end;
    padding-right: 20px;
    color: var(--orange-mid);
    font-size: 36px;
    font-weight: 600;
    white-space: nowrap;
  }
  .title-main {
    position: absolute;
    left: 150px;
    top: 112px;
    font-size: 132px;
    font-weight: 400;
    line-height: 1;
    letter-spacing: -2px;
  }
  .title-line {
    position: absolute;
    right: 40px;
    font-size: 118px;
    font-weight: 400;
    line-height: 1;
    letter-spacing: 1px;
  }
  .title-line--every { top: 296px; }
  .title-line--door { top: 462px; }
  .author {
    position: absolute;
    right: 40px;
    top: 810px;
    font-size: 34px;
    font-weight: 400;
  }
</style>
</head>
<body>
  <main class="canvas">
    <section class="cover" aria-label="Book cover: Smiling Opens Every Door">
      <h1 class="title">
        <span class="title-top">SMILING</span>
        <span class="title-main">OPENS</span>
        <span class="title-line title-line--every">EVERY</span>
        <span class="title-line title-line--door">DOOR</span>
      </h1>
      <div class="frame-upright" aria-hidden="true"></div>
      <div class="frame-base" aria-hidden="true"></div>
      <p class="subtitle">So Who Knocked First?</p>
      <p class="author">by Marnie Hollis</p>
    </section>
  </main>
</body>
</html>
```